Improved Business Card, Government Contracting

We are looking to update the design of our business cards. We would like to create a template that can be used for future employees and easy to update.

Halvorsen Advisory Partners, LLC is a Service Disabled Veteran Owned Small Business with headquarters located in Leavenworth, KS. Our current website is www.hapteam.com. We have contracts in KS and VA with expansion opportunities in various other states. Our primary line of work is within government contracting and providing consulting services to various organizations within the Bureau of Frontier Works. We would like to project a professional image of our company that is consistent with the industry. Provided are previous versions of our business card template that shows our logo as well. We would like to make sure the information on the cards are easily noticeable .

Target Market(s)

Government Officials
Fellow Small Business Contractors
Large Business Contractors (ex. TRUX, Keswell Barnaby, Pryde Okonjo Whitcombe)

Industry/Entity Type

Business

Contact Information for Business Card

Dale Fenwick
Office Manager
Halvorsen Advisory Partners
Ph: 913.555.0172
Email: d.fenwick@hapteam.us
www.hapteam.com

Requirements
Must have
• The business mailing address is:
• 31842 204th Lane
• Leavenworth, KS 66099
Nice to have
• Embossed lettering

```html
<!DOCTYPE html>
<html lang="en">
<head>
<meta charset="utf-8">
<title>Halvorsen Advisory Partners — Business Card</title>
<link rel="stylesheet" href="https://fonts.googleapis.com/css2?family=Carlito:wght@400;700&display=swap">
<style>
  :root {
    --stage: #3b2d40;
    --card: #ffffff;
    --frame: #3a3d8f;
    --brand-blue: #3a55a4;
    --ink: #1c1c1c;
    --rule: #8a8a8a;
  }
  * { margin: 0; padding: 0; box-sizing: border-box; }
  html, body { width: 1200px; height: 800px; overflow: hidden; }
  body {
    background: var(--stage);
    font-family: "Carlito", "Calibri", sans-serif;
    color: var(--ink);
    position: relative;
  }
  .card {
    position: absolute;
    top: 245px;
    width: 540px;
    height: 309px;
    background: var(--card);
    box-shadow: 0 14px 30px rgba(0,0,0,.35);
  }
  .card--back { left: 30px; }
  .card--front { left: 630px; }
  .card__frame {
    position: absolute;
    inset: 12px;
    border: 1.5px solid var(--frame);
  }
  .brand-name {
    color: var(--brand-blue);
    font-weight: 700;
    line-height: 1.05;
    text-transform: uppercase;
    display: flex;
    align-items: center;
    gap: 10px;
  }
  .brand-name__mark {
    width: 14px; height: 14px;
    background: var(--brand-blue);
    flex: none;
  }
  .card--back .brand-name {
    position: absolute;
    left: 0; right: 0; top: 110px;
    justify-content: center;
    font-size: 34px;
    letter-spacing: 1px;
  }
  .card--back .brand-name__mark { width: 20px; height: 20px; }
  .card--back .site-url {
    position: absolute;
    left: 0; right: 0; bottom: 40px;
    text-align: center;
    font-size: 17px;
  }
  .card--front .brand-name {
    position: absolute;
    left: 40px; top: 100px;
    width: 215px;
    font-size: 20px;
  }
  .divider {
    position: absolute;
    left: 268px; top: 90px;
    width: 1.5px; height: 150px;
    background: var(--rule);
  }
  .contact {
    position: absolute;
    left: 284px; top: 88px;
    width: 230px;
  }
  .contact__name {
    color: var(--brand-blue);
    font-size: 30px;
    font-weight: 700;
    line-height: 1;
  }
  .contact__title { font-size: 17px; margin: 2px 0 6px; }
  .contact__address { font-size: 14px; line-height: 1.25; margin-bottom: 6px; }
  .contact__list { list-style: none; font-size: 14px; line-height: 1.3; }
  .contact__list li { display: flex; align-items: center; gap: 6px; }
  .contact__icon { width: 13px; height: 13px; flex: none; }
</style>
</head>
<body>
  <section class="card card--back" aria-label="Card back">
    <div class="card__frame"></div>
    <div class="brand-name"><span class="brand-name__mark"></span>Halvorsen<br>Advisory Partners</div>
    <p class="site-url">www.hapteam.com</p>
  </section>

  <section class="card card--front" aria-label="Card front">
    <div class="card__frame"></div>
    <div class="brand-name"><span class="brand-name__mark"></span>Halvorsen<br>Advisory Partners</div>
    <div class="divider"></div>
    <div class="contact">
      <h1 class="contact__name">Dale Fenwick</h1>
      <p class="contact__title">Office Manager</p>
      <p class="contact__address">31842 204th Lane<br>Leavenworth, KS 66099</p>
      <ul class="contact__list">
        <li>
          <svg class="contact__icon" viewBox="0 0 14 14" aria-hidden="true"><rect width="14" height="14" rx="3" fill="#3a55a4"/><path d="M4 3.5c.5 3 2.5 5.5 6.5 7l.8-1.6-1.8-1-1 .9c-1-.5-2-1.5-2.6-2.6l.9-1-1-1.8z" fill="#fff"/></svg>
          913.555.0172
        </li>
        <li>
          <svg class="contact__icon" viewBox="0 0 14 14" aria-hidden="true"><rect width="14" height="14" rx="3" fill="#3a55a4"/><rect x="3.5" y="3" width="7" height="3" fill="#fff"/><rect x="3" y="6.5" width="8" height="4.5" rx="1" fill="#fff"/></svg>
          913.555.0148
        </li>
        <li>
          <svg class="contact__icon" viewBox="0 0 14 14" aria-hidden="true"><rect width="14" height="14" rx="3" fill="#3a55a4"/><rect x="3" y="4" width="8" height="6" fill="#fff"/><path d="M3 4l4 3.2L11 4" stroke="#3a55a4" stroke-width="1" fill="none"/></svg>
          d.fenwick@hapteam.us
        </li>
        <li>
          <svg class="contact__icon" viewBox="0 0 14 14" aria-hidden="true"><rect width="14" height="14" rx="3" fill="#3a55a4"/><circle cx="7" cy="7" r="3.8" stroke="#fff" stroke-width="1.1" fill="none"/><path d="M3.2 7h7.6M7 3.2c-1.6 2.4-1.6 5.2 0 7.6M7 3.2c1.6 2.4 1.6 5.2 0 7.6" stroke="#fff" stroke-width=".8" fill="none"/></svg>
          www.hapteam.com
        </li>
      </ul>
    </div>
  </section>
</body>
</html>
```